Vimcarra, Cosmetic skin care line

I am not looking to change my logo vimcarra on the label just want someone to design a different label I want it to be very classy as it is already just want something different. My product target classier people and people with higher income and for woman and men but mostly women. Looking to keep the label background black

Target Market(s)

Classier and higer income women/men mostly women

Industry/Entity Type

Cosmetics

• I don't really know

Colors

Designer to choose colors to be used in the design.

Requirements
Must have
• It must keep the same vimcarra logo and the same matte black background color
Nice to have
• I want a different layout and maybe different fonts for the label
Should not have

```html
<!DOCTYPE html>
<html lang="en">
<head>
<meta charset="utf-8">
<title>Vimcarra Eye Corrector Serum – Label</title>
<link rel="stylesheet" href="https://fonts.googleapis.com/css2?family=Josefin+Sans:wght@300;400&display=swap">
<style>
  :root {
    --stage: #ecece8;
    --label-black: #030303;
    --ink-white: #ffffff;
    --gold-light: #f7e7a1;
    --gold-mid: #e2b53a;
    --gold-deep: #c8921c;
  }
  html, body {
    margin: 0;
    padding: 0;
    width: 1200px;
    height: 857px;
    overflow: hidden;
    background: var(--stage);
  }
  .canvas {
    position: relative;
    width: 1200px;
    height: 857px;
  }
  .label {
    position: absolute;
    left: 120px;
    top: 47px;
    width: 960px;
    height: 763px;
    background: var(--label-black);
    font-family: "Josefin Sans", sans-serif;
    color: var(--ink-white);
  }
  .label__frame {
    position: absolute;
    left: 0;
    top: 0;
    width: 960px;
    height: 763px;
  }
  .brand {
    position: absolute;
    left: 321px;
    top: 190px;
    margin: 0;
    font-weight: 400;
    font-size: 56px;
    line-height: 1;
    letter-spacing: 0.06em;
  }
  .product {
    position: absolute;
    left: 321px;
    top: 392px;
  }
  .product__name {
    margin: 0;
    font-weight: 300;
    font-size: 56px;
    line-height: 69px;
    letter-spacing: -0.01em;
    text-transform: uppercase;
  }
  .product__rule {
    width: 88px;
    height: 3px;
    margin: 6px 0 0;
    background: var(--ink-white);
    border: 0;
  }
  .product__claim {
    margin: 18px 0 0;
    font-weight: 300;
    font-size: 18px;
    letter-spacing: 0;
    text-transform: uppercase;
  }
</style>
</head>
<body>
<main class="canvas">
  <section class="label">
    <svg class="label__frame" viewBox="0 0 960 763" aria-hidden="true">
      <defs>
        <linearGradient id="goldFoil" x1="0" y1="0" x2="1" y2="1">
          <stop offset="0" stop-color="var(--gold-mid)"/>
          <stop offset="0.35" stop-color="var(--gold-light)"/>
          <stop offset="0.6" stop-color="var(--gold-deep)"/>
          <stop offset="0.85" stop-color="var(--gold-light)"/>
          <stop offset="1" stop-color="var(--gold-mid)"/>
        </linearGradient>
      </defs>
      <rect x="34" y="45" width="892" height="675" fill="none" stroke="url(#goldFoil)" stroke-width="3"/>
    </svg>

    <p class="brand">VIMCARRA</p>

    <div class="product">
      <h1 class="product__name">Eye<br>Corrector<br>Serum</h1>
      <hr class="product__rule">
      <p class="product__claim">With Triple Peptides</p>
    </div>
  </section>
</main>
</body>
</html>
```